Business Card Design Project

We need a business card design for a new company based in Singapore called 'Bright Harbor Pte Ltd'. We provide personal development training and emotional intelligence workshops. Our slogan is "Actualize your potentials". We will not have a company address on the business card. Only phone number, email address and website address.

Target Market(s)

Adults age 25 to 45 years old.
Mostly working in a job.

Industry/Entity Type

Training

Colors
0255a2
f37123

```html
<!DOCTYPE html>
<html lang="en">
<head>
<meta charset="utf-8">
<title>Bright Harbor Pte Ltd – Business Cards</title>
<link href="https://fonts.googleapis.com/css2?family=Montserrat:wght@300;400;500;700&display=swap" rel="stylesheet">
<style>
  :root {
    --brand-blue: #0255a2;
    --brand-blue-light: #0a7cc6;
    --brand-orange: #f37123;
    --brand-navy: #1c2b5c;
    --card-white: #ffffff;
    --stage: #e9e9ec;
    --ink-grey: #4a4f5c;
  }
  * { box-sizing: border-box; margin: 0; padding: 0; }
  html, body {
    width: 1200px; height: 1000px; overflow: hidden;
    background: var(--stage);
    font-family: "Montserrat", sans-serif;
  }
  .canvas { position: relative; width: 1200px; height: 1000px; }

  .card {
    position: absolute;
    top: 200px;
    width: 380px; height: 600px;
    background: var(--card-white);
    overflow: hidden;
    box-shadow: 0 14px 30px rgba(0,0,0,0.16);
  }
  .card--front { left: 170px; }
  .card--back { left: 650px; }

  /* Front */
  .front-band {
    position: absolute; inset: 0;
    background: linear-gradient(200deg, var(--brand-blue-light), var(--brand-blue));
    clip-path: polygon(0 0, 100% 0, 100% 58%);
  }
  .front-brand {
    position: absolute;
    left: 70px; top: 250px;
    display: flex; flex-direction: column; align-items: flex-start;
  }
  .brand-dot {
    width: 30px; height: 30px; border-radius: 50%;
    background: var(--brand-blue);
    margin: 0 0 14px 20px;
  }
  .brand-lockup {
    writing-mode: vertical-rl;
    display: flex; flex-direction: column; align-items: flex-start;
  }
  .brand-name {
    font-size: 40px; font-weight: 700; color: var(--brand-navy);
    letter-spacing: -0.5px; line-height: 1.1;
  }
  .brand-suffix {
    font-size: 22px; font-weight: 400; color: var(--brand-navy);
    letter-spacing: 3px;
    padding-top: 70px; margin-right: 6px;
    border-right: 1.5px solid var(--ink-grey);
    padding-right: 4px;
    text-align: end;
  }

  /* Back */
  .back-band {
    position: absolute; inset: 0;
    background: var(--brand-orange);
    clip-path: polygon(100% 0, 100% 100%, 10% 100%);
  }
  .back-brand {
    position: absolute; left: 26px; top: 28px;
    display: flex; flex-direction: row-reverse; gap: 14px;
  }
  .back-brand .brand-name { font-size: 20px; }
  .back-brand .brand-suffix { font-size: 11px; padding-top: 30px; letter-spacing: 2px; margin-right: 3px; }
  .contact {
    writing-mode: vertical-rl;
    list-style: none;
    font-size: 14px; font-weight: 400; color: var(--brand-orange);
    line-height: 1.45;
  }
  .slogan {
    position: absolute; right: 26px; bottom: 56px;
    writing-mode: vertical-rl;
    color: var(--card-white);
    font-size: 40px; line-height: 1.1;
  }
  .slogan span { display: block; }
  .slogan__light { font-weight: 300; letter-spacing: 1px; }
  .slogan__bold { font-weight: 700; }
</style>
</head>
<body>
<main class="canvas">
  <section class="card card--front" aria-label="Business card front">
    <div class="front-band"></div>
    <div class="front-brand">
      <span class="brand-dot"></span>
      <div class="brand-lockup">
        <span class="brand-name">Bright Harbor</span>
        <span class="brand-suffix">PTE LTD</span>
      </div>
    </div>
  </section>

  <section class="card card--back" aria-label="Business card back">
    <div class="back-band"></div>
    <div class="back-brand">
      <ul class="contact">
        <li>555 - 1234</li>
        <li>website.com</li>
        <li>email@email.com</li>
      </ul>
      <div class="brand-lockup">
        <span class="brand-name">Bright Harbor</span>
        <span class="brand-suffix">PTE LTD</span>
      </div>
    </div>
    <p class="slogan">
      <span class="slogan__light">Actualize</span>
      <span class="slogan__light">your</span>
      <span class="slogan__bold">potential</span>
    </p>
  </section>
</main>
</body>
</html>
```